Brochure Design Project

I need a brochure design for a full Hair Salon, located in Rockville MD called Coralind Hair, Nails and Spa.
Please use inovative design (the idea is to target an audience between the age of 19 to 50) keeping our main colors (spring green, grey and white).
we would also like to include the list of services which will be provided when needed.

Target Market(s)

women between 19 to 50 - all ethnical backgrounds

Industry/Entity Type

Hair

Requirements
Nice to have
• we would like to include a blurb, contact info and list of prices of all the services we provided. Also we would like to add the line "se habla espaƱol" anywhere in the brochure.

```html
<!DOCTYPE html>
<html lang="en">
<head>
<meta charset="utf-8">
<title>Coralind Hair, Nails &amp; Spa – Service Menu Brochure</title>
<link href="https://fonts.googleapis.com/css2?family=Archivo+Black&family=Arimo:wght@400&family=Roboto+Slab:wght@500&display=swap" rel="stylesheet">
<style>
  :root {
    --backdrop: #c8c8c5;
    --paper: #ffffff;
    --spring: #c9dc84;
    --spring-light: #dfeaae;
    --spring-deep: #a9c25a;
    --ink: #1e1e1e;
    --rule: #3a3a3a;
    --grey-text: #555555;
  }
  * { box-sizing: border-box; margin: 0; padding: 0; }
  html, body { width: 1200px; height: 1000px; overflow: hidden; }
  body {
    background: var(--backdrop);
    font-family: "Arimo", Arial, sans-serif;
    color: var(--ink);
    position: relative;
  }
  .brochure {
    position: absolute;
    left: 60px; top: 110px;
    width: 1080px; height: 780px;
    display: flex;
    box-shadow: 0 4px 18px rgba(0,0,0,0.18);
  }
  .panel {
    position: relative;
    width: 360px; height: 780px;
    padding: 28px 36px 0;
    background: var(--paper);
  }
  .panel--hair {
    background: linear-gradient(180deg, var(--spring-light) 0%, var(--spring) 100%);
  }
  .brand {
    text-align: center;
    padding-top: 6px;
  }
  .brand__name {
    font-family: "Arimo", Arial, sans-serif;
    font-weight: 400;
    font-size: 52px;
    color: var(--spring-deep);
    line-height: 1;
  }
  .brand__tagline {
    font-size: 13px;
    color: var(--grey-text);
    margin-top: 4px;
    padding-left: 90px;
  }
  .brand__kind {
    font-family: "Roboto Slab", Georgia, serif;
    font-size: 20px;
    letter-spacing: 0.5px;
    margin-top: 2px;
  }
  .section-title {
    font-family: "Archivo Black", Impact, sans-serif;
    font-size: 26px;
    text-align: center;
    line-height: 1.1;
    margin-top: 14px;
  }
  .panel--hair .section-title,
  .panel--spa .section-title { margin-top: 0; }
  .sub-title {
    font-family: "Roboto Slab", Georgia, serif;
    font-weight: 500;
    font-size: 20px;
    text-align: center;
    letter-spacing: 0.5px;
    border-top: 2px solid var(--rule);
    border-bottom: 2px solid var(--rule);
    padding: 4px 0 3px;
    margin: 6px 0 10px;
  }
  .price-list { list-style: none; font-size: 12.5px; }
  .price-list li {
    display: flex;
    justify-content: space-between;
    line-height: 18px;
    padding-left: 14px;
  }
  .price-list .price { min-width: 44px; text-align: left; }
  .photo {
    position: absolute;
    border: 0;
  }
  .photo--hands {
    left: 0; bottom: 0; width: 360px; height: 200px;
    background: linear-gradient(135deg, #f4f4f2 0%, #edd9cc 45%, #e6c6b4 70%, #f3f3f1 100%);
  }
  .photo--stones {
    right: 16px; bottom: 12px; width: 220px; height: 96px;
    background: radial-gradient(ellipse at 40% 55%, #b8b2a8 0%, #cfcac2 40%, rgba(255,255,255,0) 72%),
                radial-gradient(circle at 82% 45%, #f08cb4 0%, rgba(255,255,255,0) 30%);
  }
  .contact {
    position: absolute;
    left: 0; right: 0; bottom: 24px;
    text-align: center;
  }
  .contact__cta { font-size: 17px; }
  .contact__phone {
    display: flex; align-items: center; justify-content: center; gap: 8px;
    font-size: 24px; margin-top: 8px;
  }
  .contact__web { font-size: 16px; margin-top: 8px; }
</style>
</head>
<body>
  <main class="brochure">
    <section class="panel panel--nails">
      <header class="brand">
        <div class="brand__name">Coralind</div>
        <div class="brand__tagline">Hair, Nails &amp; Spa</div>
        <div class="brand__kind">BEAUTY SALON</div>
      </header>
      <h2 class="section-title">NAILS</h2>
      <h3 class="sub-title">MANICURE</h3>
      <ul class="price-list">
        <li><span>Basic manicure</span><span class="price">$15</span></li>
        <li><span>Spa manicure</span><span class="price">$20</span></li>
        <li><span>Hot Oil</span><span class="price">$20</span></li>
        <li><span>French</span><span class="price">$20</span></li>
        <li><span>Gel color manicure</span><span class="price">$30</span></li>
        <li><span>Full set</span><span class="price"></span></li>
        <li><span>(classic manicure and pedicure)</span><span class="price">$35</span></li>
        <li><span>Fills</span><span class="price">$25</span></li>
      </ul>
      <h3 class="sub-title">PEDICURE</h3>
      <ul class="price-list">
        <li><span>Basic pedicure</span><span class="price">$25</span></li>
        <li><span>Warm lotion</span><span class="price">$35</span></li>
        <li><span>Spa pedicure</span><span class="price">$45</span></li>
        <li><span>Add french</span><span class="price">$5</span></li>
        <li><span>Polish change</span><span class="price">$10</span></li>
        <li><span>Designs</span><span class="price">$3</span></li>
        <li><span>Gel color (add $12) with pedicure</span><span class="price"></span></li>
      </ul>
      <div class="photo photo--hands" role="img" aria-label="Photo of manicured hands resting on one another"></div>
    </section>

    <section class="panel panel--hair">
      <h2 class="section-title">HAIR</h2>
      <h3 class="sub-title">HAIRCUTS</h3>
      <ul class="price-list">
        <li><span>Women's haircut</span><span class="price">$30</span></li>
        <li><span>Men's haircut</span><span class="price">$25</span></li>
        <li><span>Kid's haircut (8 &amp; Under)</span><span class="price">$12</span></li>
        <li><span>Kid's haircut (8 to 16)</span><span class="price">$18</span></li>
        <li><span>Girls haircut &amp; blow dry</span><span class="price">$35</span></li>
        <li><span>Hair cut &amp; blow dry</span><span class="price">$50</span></li>
        <li><span>Roller set &amp; blow dray or flat iron</span><span class="price">$55</span></li>
        <li><span>Iron or curling with service</span><span class="price">$10</span></li>
      </ul>
      <h3 class="sub-title">CONDITIONING</h3>
      <ul class="price-list">
        <li><span>Hair recovery treatment</span><span class="price">$20</span></li>
        <li><span>Deep condition</span><span class="price">$15</span></li>
        <li><span>Keratin</span><span class="price">$300+</span></li>
        <li><span>Retouch</span><span class="price">$220</span></li>
      </ul>
      <h3 class="sub-title">COLORS</h3>
      <ul class="price-list">
        <li><span>All over color</span><span class="price">$75+</span></li>
        <li><span>Color touchup</span><span class="price">$55</span></li>
        <li><span>Full highlights</span><span class="price">$125+</span></li>
        <li><span>Partial highlights</span><span class="price">$75+</span></li>
        <li><span>Corrective Color</span><span class="price">$75+</span></li>
        <li><span>Updos</span><span class="price">$65+</span></li>
      </ul>
      <h3 class="sub-title">PERMS</h3>
      <ul class="price-list">
        <li><span>Relaxer with haircut style</span><span class="price">$85</span></li>
        <li><span>Curly Perms</span><span class="price">$95+</span></li>
      </ul>
      <footer class="contact">
        <p class="contact__cta">Call in advance for an appointment!</p>
        <p class="contact__phone">
          <svg width="20" height="20" viewBox="0 0 20 20" aria-hidden="true">
            <circle cx="10" cy="10" r="9" fill="none" stroke="#1e1e1e" stroke-width="1.2"/>
            <path d="M7 5.5c-.8.4-1.3 1.2-1 2.3.6 2.4 2.6 4.6 5 5.5 1 .4 1.9 0 2.4-.8l-1.6-1.5-1 .6c-1-.5-1.9-1.5-2.3-2.5l.7-.9z" fill="#1e1e1e"/>
          </svg>
          301-555-0148
        </p>
        <p class="contact__web">www.coralindhns.com</p>
      </footer>
    </section>

    <section class="panel panel--spa">
      <h2 class="section-title">SPA</h2>
      <h3 class="sub-title">FACIALS</h3>
      <ul class="price-list">
        <li><span>European facial</span><span class="price">$85</span></li>
        <li><span>Multi Vitamin facial</span><span class="price">$85</span></li>
        <li><span>Acne facial</span><span class="price">$80</span></li>
        <li><span>Gentleman facial</span><span class="price">$75</span></li>
        <li><span>Lunch break facial</span><span class="price">$45</span></li>
        <li><span>Teen facial</span><span class="price">$50</span></li>
        <li><span>Mini facial</span><span class="price">$45</span></li>
        <li><span>Anti aging facial</span><span class="price">$120</span></li>
        <li><span>Gold facial</span><span class="price">$60</span></li>
        <li><span>Fruit facial</span><span class="price">$45</span></li>
        <li><span>Special bridal facial</span><span class="price">$130</span></li>
      </ul>
      <h3 class="sub-title">MASSAGES</h3>
      <ul class="price-list">
        <li><span>Scalp massages 10 min</span><span class="price">$15</span></li>
        <li><span>Head &amp; neck massage 15 min</span><span class="price">$20</span></li>
        <li><span>Back massage 15 min</span><span class="price">$20</span></li>
        <li><span>Full body massage 60 min</span><span class="price">$75</span></li>
        <li><span>Full body massage 30 min</span><span class="price">$40</span></li>
        <li><span>Foot massage 10 min</span><span class="price">$15</span></li>
        <li><span>Half leg &amp; foot 15 min</span><span class="price">$20</span></li>
      </ul>
      <h3 class="sub-title">MASSAGES</h3>
      <ul class="price-list price-list--threading">
        <li><span>Eyebrow threading</span><span class="price">$12</span></li>
        <li><span>Chin Threading</span><span class="price">$8</span></li>
        <li><span>Upper lip</span><span class="price">$7</span></li>
        <li><span>Lower lip</span><span class="price">$7</span></li>
        <li><span>Forehead</span><span class="price">$10</span></li>
        <li><span>Side burns</span><span class="price">$10</span></li>
        <li><span>Full Face</span><span class="price">$40+</span></li>
      </ul>
      <div class="photo photo--stones" role="img" aria-label="Photo of stacked spa stones beside a pink daisy"></div>
    </section>
  </main>
</body>
</html>
```